Brindlecove Flood Restoration needing website

Hi Team

We are looking for a 4 or 5 page website containing
1: Home
2: Services
3: Gallery
4: Equipment Hire
5 Contact Us

Would want the front page to be a big call to action. Someones house has just flooded...they're highly stressed and we just want to let them know straight away that we can assist them

Some call to action would be great.

"Wet Carpets??"

"Washing machine just overflowed??"

"Burst pipe?"

"We're here to help!!"

Would be wanting a scrolling banner type homepage with images of flooded houses, heavy rain, a mother in shock that the house has been flooded by an overflowing washing machine, someone taking an emergency call with text saying that we are there to take your call 24/7 365 days a year

Target Market(s)

insurance companies and home owners

Industry/Entity Type

Hire

Coding

Coded - Design and coding required

Number of Pages Required

5+ page

Requirements
Must have
• 24/7 emergency contact number on home page (0498215763)
• 4 photos on banner on home page
• Equipment Hire Page should include images and brief description of these 3 products
• http://www.ptkdirect.example.com.au/prod458.htm
• http://www.gustline-gear.example.com.au/product/mistral-breeze-fan/
• http://www.vendrasuck.example.com.au/carpet/carpet-extractor-harrier-xv-x-vi-x-vii
• SERVICES OFFERED ARE:
• 24/7 Emergnecy Flood Restoration
• Insurance Claims
• Structural Drying
• Sub Floor Drying
• Supply and installation of drying equipment
• Professional Carpet and underlay installation
Nice to have
• Some other websites we like
• www.kelbyleakfixers.example.com.au
• www.summitrecoverywashing.example.com.au/flood-water-damage-restoration
• http://www.pelhamrecovery.example.com.au/
• http://www.dampfixnational.example.com.au/
Should not have
• not looking for an all white background.

```html
<!DOCTYPE html>
<html lang="en">
<head>
<meta charset="utf-8">
<title>Brindlecove Flood Restoration – Home</title>
<link href="https://fonts.googleapis.com/css2?family=Montserrat:ital,wght@0,400;0,500;0,600;0,700;1,400&family=Raleway:wght@400;500&display=swap" rel="stylesheet">
<style>
:root{
  --slate:#5a6577;
  --sky:#3bb9f4;
  --teal:#0ab0b8;
  --yellow:#f2ec24;
  --yellow-soft:rgba(240,236,60,.72);
  --ink:#161616;
  --navy:#2e4a7a;
  --red:#ff4a1c;
  --mint:#e8f6f8;
  --charcoal:#474747;
  --icon-grey:#4c4c4c;
  --white:#fff;
  --scene:
    radial-gradient(ellipse 30% 18% at 48% 62%, rgba(245,243,238,.85), rgba(245,243,238,0) 100%),
    radial-gradient(ellipse 16% 20% at 14% 48%, rgba(220,214,204,.9), rgba(220,214,204,0) 100%),
    radial-gradient(ellipse 40% 22% at 58% 22%, rgba(150,146,140,.45), rgba(150,146,140,0) 100%),
    radial-gradient(ellipse 22% 14% at 12% 14%, rgba(160,156,150,.4), rgba(160,156,150,0) 100%),
    linear-gradient(180deg,#d4d0ca 0%,#c8c4be 40%,#c2bcb3 66%,#a99a82 72%,#c7bba6 80%,#b09f86 88%,#cdc2ae 100%);
}
*{margin:0;padding:0;box-sizing:border-box}
html,body{width:1200px;height:1200px;overflow:hidden}
body{background:var(--slate);font-family:"Montserrat",sans-serif;color:var(--ink);position:relative}
.abs{position:absolute}

/* large page view */
.page{left:96px;top:0;width:1024px;height:1200px;background:var(--white);overflow:hidden}
.topbar{left:0;top:0;width:100%;height:48px;background:var(--sky);color:var(--white);font-size:16px}
.topbar .mail{left:118px;top:15px}
.social{display:flex;gap:8px}
.social span{width:26px;height:26px;background:rgba(255,255,255,.35);display:block}
.topbar .social{left:628px;top:11px}
.topbar .contact{left:824px;top:14px}
.brand{display:flex;align-items:center;gap:12px;color:#1d8fd6;font-weight:600}
.site-header .brand{left:118px;top:92px;font-size:22px}
.brand i{display:block;width:34px;height:34px;background:#1d8fd6}
.nav{display:flex;gap:24px;font-weight:600;color:var(--navy);font-size:13px}
.site-header .nav{left:564px;top:110px}
.nav .active{color:var(--red);border-bottom:4px solid var(--red);padding-bottom:2px}
.hero{left:0;top:172px;width:100%;height:388px;background:var(--scene)}
.hero-border{left:0;top:556px;width:100%;height:6px;background:#555}
.hero-tag{left:309px;top:129px;width:420px;height:111px;background:var(--yellow-soft)}
.hero-tag h1{position:absolute;left:17px;top:10px;font-weight:400;font-size:58px;white-space:nowrap}
.hero-tag p{position:absolute;left:230px;top:72px;font-size:34px;white-space:nowrap}
.arrow{left:124px;top:180px}
.call-bar{left:330px;top:536px;width:365px;height:42px;background:var(--yellow);font-weight:600;font-size:22px;text-align:center;line-height:42px;box-shadow:0 3px 4px rgba(0,0,0,.35);letter-spacing:.5px}
.about-title{left:0;width:1024px;top:624px;text-align:center;font-family:"Raleway",sans-serif;color:var(--sky);font-size:49px;font-weight:500}
.about-text{left:0;width:1024px;top:692px;text-align:center;font-size:19px;line-height:29px;font-weight:500}
.know{left:0;width:1024px;top:820px;text-align:center;font-weight:700;font-size:18px;letter-spacing:.5px}
.emergency{left:0;top:867px;width:100%;height:287px;background:var(--teal);color:var(--white)}
.emergency svg{position:absolute;left:148px;top:43px}
.emergency h2{position:absolute;left:412px;top:40px;font-size:40px;font-weight:500;white-space:nowrap}
.emergency p{position:absolute;left:412px;top:112px;font-style:italic;font-size:23px;line-height:29px;white-space:nowrap}
.services-title{left:0;width:1024px;top:1168px;text-align:center;font-family:"Raleway",sans-serif;color:var(--sky);font-size:49px;font-weight:500}

/* full page thumbnail */
.thumb{left:814px;top:58px;width:358px;height:1118px;background:var(--white);overflow:hidden;box-shadow:-6px 4px 14px rgba(0,0,0,.55);font-size:6px}
.t-bar{left:0;top:0;width:100%;height:16px;background:var(--sky);color:var(--white);font-size:5px}
.t-bar .mail{left:41px;top:5px}
.t-bar .social{left:220px;top:4px;gap:3px}
.t-bar .social span{width:8px;height:8px}
.t-bar .contact{left:288px;top:5px}
.thumb .brand{left:42px;top:32px;font-size:7px;gap:4px}
.thumb .brand i{width:12px;height:12px}
.thumb .nav{left:198px;top:38px;font-size:4px;gap:7px}
.thumb .nav .active{border-bottom-width:1px}
.t-hero{left:0;top:60px;width:100%;height:137px;background:var(--scene);border-bottom:2px solid #555}
.t-hero .tag{left:108px;top:46px;width:183px;height:38px;background:var(--yellow-soft)}
.t-hero .tag b{position:absolute;left:5px;top:2px;font-weight:400;font-size:18px;white-space:nowrap}
.t-hero .tag span{position:absolute;left:79px;top:24px;font-size:9px;white-space:nowrap}
.t-arrow{top:64px}
.t-call{left:114px;top:186px;width:128px;height:16px;background:var(--yellow);font-weight:600;font-size:6.5px;text-align:center;line-height:16px}
.t-h{left:0;width:358px;text-align:center;font-family:"Raleway",sans-serif;color:var(--sky);font-size:14px;font-weight:500}
.t-p{left:0;width:358px;text-align:center;font-size:5.6px;line-height:10px;font-weight:500}
.t-sub{left:0;width:358px;text-align:center;color:var(--sky);font-size:5px;line-height:8px}
.t-emerg{left:0;top:303px;width:100%;height:100px;background:var(--teal);color:var(--white)}
.t-emerg svg{position:absolute;left:52px;top:14px}
.t-emerg h3{position:absolute;left:144px;top:16px;font-size:11px;font-weight:500;white-space:nowrap}
.t-emerg p{position:absolute;left:144px;top:38px;font-style:italic;font-size:6.6px;line-height:10px;white-space:nowrap}
.svc-dot{width:36px;height:36px;border-radius:50%;background:radial-gradient(circle at 55% 45%,#e8d020 0 30%,#2d3540 60%);border:2px solid var(--teal)}
.svc-label{font-size:5.5px;line-height:7px;text-align:center;width:70px}
.worker{left:124px;top:470px;width:88px;height:156px;background:linear-gradient(180deg,#e9c24a 0%,#4a6f93 35%,#34495e 100%);border-radius:40px 40px 4px 4px}
.t-stats{left:0;top:626px;width:100%;height:100px;background:var(--sky);color:var(--white);display:flex;justify-content:space-around;padding:27px 20px 0}
.t-stats div{text-align:center;font-size:8.5px;line-height:11px}
.t-stats b{display:block;font-size:14px;font-weight:600;line-height:16px}
.t-clients{left:0;top:726px;width:100%;height:178px;background:var(--mint)}
.avatar{left:162px;top:62px;width:34px;height:34px;border-radius:50%;background:radial-gradient(circle at 55% 45%,#e8d020 0 30%,#2d3540 60%);border:2px solid var(--teal)}
.t-name{top:100px;font-size:6.5px;line-height:8px;font-weight:600}
.t-badges{left:0;top:904px;width:100%;height:82px;display:flex;gap:13px;padding:22px 0 0 44px}
.t-badges span{display:block;width:32px;height:44px;border-radius:3px;background:#cfd8e0}
.t-badges span:nth-child(2){background:#b9d8a8}
.t-badges span:nth-child(3){background:#e6a7a4}
.t-badges span:nth-child(4){background:#e4e0d2}
.t-badges span:nth-child(5){background:#3b4f60}
.t-badges span:nth-child(6){width:56px;height:24px;margin-top:8px;background:#c5d5ec}
.t-foot{left:0;top:986px;width:100%;height:110px;background:var(--charcoal);color:#ddd;font-size:3.6px;line-height:5px}
.t-foot h4{font-size:4.4px;font-weight:600;margin-bottom:9px;color:#fff}
.col{position:absolute;top:10px;width:70px}
.field{width:43px;height:5px;background:#fff;margin-bottom:4px;color:#666;font-size:3px;padding-left:2px;line-height:5px}
.btn{width:22px;height:5px;background:var(--sky);color:#fff;font-size:3px;line-height:5px;text-align:center}
.t-foot .social{left:40px;top:86px;gap:3px}
.t-foot .social span{width:8px;height:8px;background:var(--sky)}
.t-copy{left:0;top:1096px;width:100%;height:22px;font-size:4.6px;color:#333}
.t-copy span{position:absolute;left:41px;top:8px}
</style>
</head>
<body>

<svg width="0" height="0" style="position:absolute">
  <symbol id="icon-24" viewBox="0 0 200 200">
    <circle cx="100" cy="100" r="92" fill="none" stroke="currentColor" stroke-width="12"/>
    <path d="M100 38 A62 62 0 1 1 42 82" fill="none" stroke="currentColor" stroke-width="9"/>
    <path d="M52 62 c-10 6 -14 18 -10 32 c10 34 34 60 66 74 c14 6 26 2 32 -8 l6 -10 l-24 -16 l-12 12 c-18 -8 -34 -26 -42 -44 l12 -12 l-14 -26 z" fill="currentColor"/>
    <text x="106" y="110" font-family="Montserrat, sans-serif" font-weight="700" font-size="48" fill="currentColor" text-anchor="middle">24</text>
  </symbol>
</svg>

<main class="page abs">
  <div class="topbar abs">
    <span class="mail abs">info@brindlecove.example.com</span>
    <div class="social abs"><span></span><span></span><span></span><span></span><span></span></div>
    <span class="contact abs">Contact Us</span>
  </div>
  <header class="site-header">
    <div class="brand abs"><i></i>Brindlecove Flood Restoration</div>
    <nav class="nav abs"><span class="active">HOME</span><span>SERVICES</span><span>GALLERY</span><span>EQUIPMENTS HIRE</span></nav>
  </header>
  <section class="hero abs" role="img" aria-label="Photo of a flooded living room with a white sofa, side table and lamp standing in water">
    <div class="hero-tag abs"><h1>Wet Carpets?</h1><p>We're here to help!</p></div>
    <svg class="arrow abs" width="26" height="44" viewBox="0 0 26 44"><path d="M22 4 L6 22 L22 40" fill="none" stroke="var(--yellow)" stroke-width="5"/></svg>
  </section>
  <div class="hero-border abs"></div>
  <div class="call-bar abs">Emergency Call : 0498215763</div>
  <h2 class="about-title abs">ABOUT US</h2>
  <p class="about-text abs">Lorem ipsum dolor sit amet, consectetur adipiscing elit. Fusce accumsan<br>ac ex non tempor. In ullamcorper placerat feugiat. Vestibulum luctus ele-<br>mentum nisl, vitae auctor tortor cursus vel. Donec porta luctus metus.</p>
  <p class="know abs">Know More...</p>
  <section class="emergency abs">
    <svg width="200" height="200" style="color:var(--icon-grey)"><use href="#icon-24"/></svg>
    <h2>24/7 Emergency Service</h2>
    <p>If flooding has occurred to your home it<br>really is important to act fast the sooner the<br>water is removed and your property dried the<br>better.</p>
  </section>
  <h2 class="services-title abs">OUR SERVICES</h2>
</main>

<aside class="thumb abs">
  <div class="t-bar abs">
    <span class="mail abs">info@brindlecove.example.com</span>
    <div class="social abs"><span></span><span></span><span></span><span></span><span></span></div>
    <span class="contact abs">Contact Us</span>
  </div>
  <div class="brand abs"><i></i>Brindlecove Flood Restoration</div>
  <nav class="nav abs"><span class="active">HOME</span><span>SERVICES</span><span>GALLERY</span><span>EQUIPMENTS HIRE</span></nav>
  <div class="t-hero abs" role="img" aria-label="Photo of a flooded living room with sofa, lamp and potted tree">
    <div class="tag abs"><b>Wet Carpets?</b><span>We're here to help!</span></div>
    <svg class="t-arrow abs" style="left:22px" width="10" height="16" viewBox="0 0 10 16"><path d="M8 2 L2 8 L8 14" fill="none" stroke="var(--yellow)" stroke-width="2"/></svg>
    <svg class="t-arrow abs" style="left:326px" width="10" height="16" viewBox="0 0 10 16"><path d="M2 2 L8 8 L2 14" fill="none" stroke="var(--yellow)" stroke-width="2"/></svg>
  </div>
  <div class="t-call abs">Emergency Call : 0498215763</div>

  <h3 class="t-h abs" style="top:218px">ABOUT US</h3>
  <p class="t-p abs" style="top:242px">Lorem ipsum dolor sit amet, consectetur adipiscing elit. Fusce accumsan<br>ac ex non tempor. In ullamcorper placerat feugiat. Vestibulum luctus ele-<br>mentum nisl, vitae auctor tortor cursus vel. Donec porta luctus metus.</p>
  <p class="t-p abs" style="top:286px;font-weight:700">Know More...</p>

  <section class="t-emerg abs">
    <svg width="72" height="72" style="color:var(--icon-grey)"><use href="#icon-24"/></svg>
    <h3>24/7 Emergency Service</h3>
    <p>If flooding has occurred to your home it<br>really is important to act fast the sooner the<br>water is removed and your property dried the<br>better.</p>
  </section>

  <h3 class="t-h abs" style="top:409px">OUR SERVICES</h3>
  <p class="t-sub abs" style="top:428px">Lorem ipsum dolor sit amet, consectetur adipiscing elit. Fusce ac-<br>cumsan ac ex non tempor.</p>
  <div class="svc-dot abs" style="left:47px;top:458px" role="img" aria-label="Service icon photo"></div>
  <div class="svc-dot abs" style="left:47px;top:517px" role="img" aria-label="Service icon photo"></div>
  <div class="svc-dot abs" style="left:47px;top:582px" role="img" aria-label="Service icon photo"></div>
  <div class="svc-dot abs" style="left:275px;top:458px" role="img" aria-label="Service icon photo"></div>
  <div class="svc-dot abs" style="left:275px;top:517px" role="img" aria-label="Service icon photo"></div>
  <div class="svc-dot abs" style="left:275px;top:582px" role="img" aria-label="Service icon photo"></div>
  <p class="svc-label abs" style="left:76px;top:466px">24/7<br>Flood Restoration</p>
  <p class="svc-label abs" style="left:72px;top:530px">Structural<br>Drying</p>
  <p class="svc-label abs" style="left:68px;top:597px">Sub Floor<br>Drying</p>
  <p class="svc-label abs" style="left:212px;top:463px">Supply<br>&amp; installation<br>of drying<br>equipment</p>
  <p class="svc-label abs" style="left:212px;top:524px">Professional<br>Carpet and<br>underlay<br>installation</p>
  <p class="svc-label abs" style="left:212px;top:600px">Insurance<br>reporting</p>
  <div class="worker abs" role="img" aria-label="Photo of a tradesman in hard hat holding a toolbox"></div>

  <section class="t-stats abs">
    <div><b>1000+</b>Satisfied<br>Customers</div>
    <div><b>3000+</b>Jobs<br>Completed</div>
    <div><b>25+</b>Trained<br>Team Members</div>
  </section>

  <section class="t-clients abs">
    <h3 class="t-h abs" style="top:14px">WORDS OF CLIENTS</h3>
    <p class="t-sub abs" style="top:33px">Lorem ipsum dolor sit amet, consectetur adipiscing elit. Fusce ac-<br>cumsan ac ex non tempor.</p>
    <div class="avatar abs" role="img" aria-label="Client portrait photo"></div>
    <p class="t-p t-name abs">Marlo T<br>CEO</p>
    <p class="t-p abs" style="top:124px">Lorem ipsum dolor sit amet, consectetur adipiscing elit. Fusce accumsan<br>ac ex non tempor. In ullamcorper placerat feugiat. Vestibulum luctus ele-<br>mentum nisl, vitae auctor tortor cursus vel. Donec porta luctus metus.</p>
  </section>

  <div class="t-badges abs" role="img" aria-label="Certification and membership badges">
    <span></span><span></span><span></span><span></span><span></span><span></span>
  </div>

  <footer class="t-foot abs">
    <div class="col" style="left:40px"><h4>Brindlecove</h4>Lorem ipsum dolor sit amet, consectetur adipiscing elit. Fusce accumsan ac ex non tempor. In ullamcorper placerat feugiat. Vestibulum luctus elementum nisl, vitae auctor tortor cursus vel.</div>
    <div class="col" style="left:122px"><h4>Quick Links</h4>Privacy Policy<br>Disclaimer<br>Terms &amp; Conditions</div>
    <div class="col" style="left:193px"><h4>Contact Us</h4>12, Harbour Lane,<br>Riverside Road,<br>Brindle Bay - 4000<br><br>help@brindlecove.example.com<br>+61-400111222</div>
    <div class="col" style="left:273px"><h4>Newsletter</h4><div class="field">Name</div><div class="field">E-mail</div><div class="btn">Subscribe</div></div>
    <div class="social abs"><span></span><span></span><span></span><span></span><span></span></div>
  </footer>
  <div class="t-copy abs"><span>(c) 2016 ALL RIGHTS RESERVED BRINDLECOVE.EXAMPLE.COM</span></div>
</aside>

</body>
</html>
```